REDESIGN SIGN UP PAGE - EASY TO READ AND UNDERSTAND QUICKLY

I need to redesign my sign up page DESKTOP AND MOBILE VERSION to include 2 products that are each available as a monthly subscription, 6 mth or 12 mth subscription.

Currently I only promote one product on my website but now will be two. https://www.brightlanepromoworks.biz/signup

Now I will have two products:

1. UNLIMITED VACATION CERTIFICATES, DINING VOUCHERS & SAVINGS INCENTIVES
Unlimited Monthly Plan $99 / Month + $199 One-Time Set-Up Fee
Unlimited Bi Annual Plan $490 / 6 Months + $199 One-Time Set-Up Fee
Unlimited Annual Plan $898 / 12 Months + $199 One-Time Set-Up Fee

2. UNLIMITED SMART DEVICE INCENTIVES & OTHER HARD PREMIUMS
Unlimited Monthly Plan $299 / Month + $199 One-Time Set-Up Fee
Unlimited Bi Annual Plan $1,590 / 6 Months + $199 One-Time Set-Up Fee
Unlimited Annual Plan $2,898 / 12 Months + $199 One-Time Set-Up Fee

When promoting the different plans you can see the different categories of incentives I offer here: https://www.brightlanepromoworks.biz/incentives

The SMART DEVICE CERTIFICATES & INCENTIVES category is for product #2 and all the rest of the Categories is for Product #1 Feel free to use images as a visual so customers can see that this product includes Vacations & Restaurants and this product includes only smart devices....

USE ALL CURRENT BULLET POINTS FOR BOTH PLANS THAT IS CURRENTLY ON WEBSITE. USE ALL CURRENT CONTENT ON WEBSITE ORIGINAL SIGN UP PAGE. DO NOT LEAVE ANY CONTENT OUT.

Target Market(s)

BUSINESS OWNERS

Industry/Entity Type

Marketing

Number of Pages Required

2 page

Requirements
Must have
• When promoting the 2 different products on the new sign up page you can see the different categories of incentives I offer here: https://www.brightlanepromoworks.biz/incentives fee; free to use images to showcase what each product offers.

The SMART DEVICE CERTIFICATES & INCENTIVES category is for product #2 and all the rest of the Categories is for Product #1

I want the user to easily understand we have two products that are available in 3 ways, monthly subscription, bi annual and annual and can see the price immediately for all 3 options for both products without toggling, etc.

Must be super clean easy to ready design. Not too busy at all please
Nice to have
• USE ALL CURRENT BULLET POINTS FOR BOTH PLANS THAT IS CURRENTLY ON WEBSITE. USE ALL CURRENT CONTENT ON WEBSITE ORIGINAL SIGN UP PAGE. DO NOT LEAVE ANY CONTENT OUT.

Should not have

```html
<!DOCTYPE html>
<html lang="en">
<head>
<meta charset="utf-8">
<title>Sign Up – Bright Lane Promo Works</title>
<link href="https://fonts.googleapis.com/css2?family=Montserrat:ital,wght@0,500;0,600;0,700;0,800;0,900;1,400&family=Poppins:ital,wght@0,300;0,400;0,500;0,600;1,400&display=swap" rel="stylesheet">
<style>
:root{
  --blue:#1a6fc4;
  --blue-nav:#1976cc;
  --green:#4caf50;
  --red:#e8202a;
  --ink:#111;
  --grey:#555;
  --footer:#0f1b28;
  --footer-text:#b7c0cc;
  --white:#fff;
}
*{margin:0;padding:0;box-sizing:border-box}
html,body{width:1200px;height:2530px;overflow:hidden;background:#fff}
body{position:relative;font-family:'Poppins',sans-serif;color:var(--ink)}

/* header */
.site-header{position:absolute;left:0;top:0;width:1200px;height:68px;background:var(--blue-nav)}
.header-shape{position:absolute;left:0;top:0}
.brand{position:absolute;left:22px;top:17px;display:flex;align-items:center;gap:8px}
.brand-dot{width:26px;height:26px;border-radius:50%;background:var(--blue)}
.brand-name{font-family:'Montserrat',sans-serif;font-weight:700;font-size:14px;line-height:16px;color:var(--blue);letter-spacing:.5px}
.main-nav{position:absolute;left:358px;top:0;height:68px;display:flex;align-items:center}
.main-nav a{color:#fff;text-decoration:none;font-size:10.5px;padding:0 8px;border-right:1px solid rgba(255,255,255,.35);line-height:12px}
.main-nav a:last-child{border-right:0}
.nav-box{position:absolute;top:0;height:68px;display:flex;flex-direction:column;align-items:center;justify-content:center;color:#fff;font-size:9.5px;gap:4px}
.nav-login{left:850px;width:67px;background:#3c4756}
.nav-signup{left:917px;width:68px;background:var(--blue-nav)}
.nav-call{left:985px;width:215px;background:var(--green);flex-direction:row;justify-content:flex-start;padding-left:8px;gap:10px}
.nav-call p{font-size:10.5px;font-weight:600;line-height:16px}

/* hero */
.hero{position:absolute;left:0;top:68px;width:1200px;height:407px;background:linear-gradient(90deg,#8fd3e2 0%,#6dc8dd 55%,#4bb7d2 100%)}
.hero-photo{position:absolute;right:0;top:0;width:480px;height:407px;background:linear-gradient(135deg,rgba(228,92,76,.35),rgba(47,107,70,.35))}
.hero-title{position:absolute;left:128px;top:98px;font-family:'Montserrat',sans-serif;font-weight:900;font-size:80px;line-height:74px;color:#fff;letter-spacing:-1px}

/* intro */
.intro-title{position:absolute;left:0;top:560px;width:1200px;text-align:center;font-family:'Montserrat',sans-serif;font-weight:900;font-size:42px;line-height:58px;letter-spacing:-.8px;color:var(--ink)}
.intro-title span{color:var(--blue)}
.intro-text{position:absolute;left:0;top:715px;width:1200px;text-align:center;font-weight:300;font-size:26px;line-height:41px;color:var(--grey)}

/* plans */
.plan{position:absolute;top:908px;width:329px;height:1088px;color:#fff}
.plan-body{position:absolute;inset:0;border-radius:34px;overflow:hidden;background:linear-gradient(180deg,var(--c1) 0%,var(--c2) 100%)}
.plan-body::before{content:"";position:absolute;left:-60px;top:-110px;width:449px;height:290px;border-radius:0 0 50% 50%;background:var(--c3)}
.plan-body::after{content:"";position:absolute;left:0;top:0;width:100%;height:18px;background:var(--c4)}
.plan-monthly{left:74px;--c1:#4caf50;--c2:#2f7d33;--c3:#3f9a43;--c4:#24702a;--ring:#4caf50}
.plan-biannual{left:435px;--c1:#ec1c24;--c2:#b3131a;--c3:#d21820;--c4:#8e0e13;--ring:#e8202a}
.plan-annual{left:795px;--c1:#1a73c2;--c2:#0f5295;--c3:#1463ad;--c4:#0d4a84;--ring:#1a6fc4}
.plan-price{position:absolute;left:40px;top:-62px;width:250px;height:250px;border-radius:50%;background:#fff;border:4px solid var(--ring);display:flex;flex-direction:column;align-items:center;justify-content:center;color:#333}
.price-label{font-family:'Montserrat',sans-serif;font-weight:700;font-size:10.5px;letter-spacing:.8px;color:var(--ring);text-transform:uppercase}
.price-value{font-family:'Montserrat',sans-serif;font-weight:800;font-size:44px;line-height:50px;letter-spacing:-1px}
.price-split{width:130px;height:1px;background:#d5d5d5;margin:7px 0 9px}
.plan-head{position:absolute;left:0;top:240px;width:100%;text-align:center}
.plan-kicker{font-weight:500;font-size:14px}
.plan-name{font-family:'Montserrat',sans-serif;font-weight:800;font-size:44px;line-height:50px;margin-top:2px}
.plan-rule{width:248px;height:1px;background:rgba(255,255,255,.8);margin:8px auto 0}
.plan-fee{font-style:italic;font-size:12px;margin-top:13px}
.plan-list{position:absolute;left:32px;top:396px;list-style:none}
.plan-list li{position:relative;padding-left:20px;font-size:10.6px;line-height:28.3px;white-space:nowrap}
.plan-list li::before{content:"";position:absolute;left:0;top:9px;width:11px;height:11px;border-radius:50%;background:#fff}
.plan-list li::after{content:"";position:absolute;left:3.5px;top:11.5px;width:3px;height:5px;border:solid var(--ring);border-width:0 1.6px 1.6px 0;transform:rotate(45deg)}
.plan-actions{position:absolute;left:24px;top:994px;width:281px;display:flex;gap:11px}
.plan-select{flex:1;height:51px;border-radius:26px;background:#fff;color:#111;display:flex;flex-direction:column;align-items:center;justify-content:center;line-height:15px}
.plan-select strong{font-weight:600;font-size:14px;letter-spacing:.3px}
.plan-select small{font-size:9.5px;color:#555}

/* footer */
.site-footer{position:absolute;left:0;top:2072px;width:1200px;height:458px;background:var(--footer);color:var(--footer-text);font-size:11.5px}
.footer-brand{position:absolute;left:92px;top:70px;width:240px;display:flex;align-items:center;gap:10px;justify-content:center}
.footer-brand .brand-dot{width:30px;height:30px}
.footer-brand .brand-name{font-size:17px;line-height:20px}
.social{position:absolute;left:124px;top:158px;display:flex;gap:10px}
.social span{width:37px;height:37px;border-radius:50%;background:#6b7482}
.samples-btn{position:absolute;left:96px;top:218px;width:231px;height:52px;background:var(--green);border-radius:3px 3px 12px 12px;color:#fff;text-align:center;padding-top:8px}
.samples-btn strong{display:block;font-family:'Montserrat',sans-serif;font-weight:800;font-size:14px;letter-spacing:-.3px}
.samples-btn em{font-style:normal;font-size:11px}
.footer-col{position:absolute;top:68px}
.footer-col h3{font-family:'Montserrat',sans-serif;font-weight:800;font-size:15px;color:#fff;letter-spacing:-.3px;margin-bottom:16px}
.col-contact{left:375px;width:290px}
.col-quick{left:700px;width:160px}
.col-other{left:896px;width:230px}
.divider{position:absolute;top:68px;width:1px;height:280px;background:#2d3a4a}
.footer-col ul{list-style:none}
.footer-col li{line-height:17px;margin-bottom:8px}
.contact-row{position:relative;padding-left:24px;line-height:17px;margin-bottom:8px}
.contact-row svg{position:absolute;left:0;top:2px}
.contact-row b{color:#fff;font-weight:600}
.contact-row .hi{color:var(--green)}
.copyright{position:absolute;left:92px;top:436px;font-size:12px}
.copyright b{color:#fff;font-weight:600}
.copyright .hi{color:#2f8ee8}
.legal{position:absolute;left:882px;top:436px;font-size:12px}
.chat{position:absolute;left:1128px;top:406px;width:46px;height:46px;border-radius:50%;background:#e5242b;display:flex;align-items:center;justify-content:center}
</style>
</head>
<body>

<header class="site-header">
  <svg class="header-shape" width="360" height="68" viewBox="0 0 360 68" aria-hidden="true">
    <polygon points="0,0 336,0 320,68 0,68" fill="#2a8ad8"/>
    <polygon points="0,0 326,0 310,68 0,68" fill="#fff"/>
  </svg>
  <div class="brand"><span class="brand-dot"></span><span class="brand-name">BRIGHT LANE<br>PROMO WORKS</span></div>
  <nav class="main-nav">
    <a>Home</a><a>The Incentives</a><a>Samples</a><a>Industries</a><a>Testimonials</a><a>Faq</a><a>Integrations</a>
  </nav>
  <div class="nav-box nav-login">
    <svg width="16" height="16" viewBox="0 0 16 16" aria-hidden="true"><circle cx="8" cy="5" r="3.5" fill="#fff"/><path d="M1 16c0-4 3-6 7-6s7 2 7 6z" fill="#fff"/></svg>
    LOGIN
  </div>
  <div class="nav-box nav-signup">
    <svg width="18" height="18" viewBox="0 0 18 18" aria-hidden="true"><circle cx="9" cy="9" r="8" fill="none" stroke="#fff" stroke-width="1.5"/><path d="M9 13V5M5.5 8.5L9 5l3.5 3.5" fill="none" stroke="#fff" stroke-width="1.8"/></svg>
    SIGN UP
  </div>
  <div class="nav-box nav-call">
    <svg width="16" height="30" viewBox="0 0 16 30" aria-hidden="true"><rect x="1" y="1" width="14" height="28" rx="2.5" fill="none" stroke="#fff" stroke-width="2"/><circle cx="8" cy="25" r="1.5" fill="#fff"/></svg>
    <p>CALL US: 1-555-014-2286<br>TEXT US: 1-555-014-7712</p>
  </div>
</header>

<section class="hero">
  <div class="hero-photo" role="img" aria-label="Travel flat lay on turquoise: red passport, toy airplane, straw hat, toy bus and palm leaf"></div>
  <h1 class="hero-title">VACATION<br>DINING<br>SAVINGS</h1>
</section>

<h2 class="intro-title">CONGRATULATIONS ON MAKING THE DECISION<br>TO <span>MAKE MORE MONEY FOR YOUR BUSINESS</span></h2>
<p class="intro-text">This program is an online subscription based incentive marketing<br>system with the following features</p>

<article class="plan plan-monthly">
  <div class="plan-body"></div>
  <div class="plan-price">
    <span class="price-label">Vacation &amp; Dining</span><span class="price-value">$99</span>
    <span class="price-split"></span>
    <span class="price-label">Smart Devices</span><span class="price-value">$299</span>
  </div>
  <div class="plan-head">
    <p class="plan-kicker">Unlimited Plan</p>
    <h3 class="plan-name">MONTHLY</h3>
    <div class="plan-rule"></div>
    <p class="plan-fee">Month + $199 One-Time Set-Up Fee</p>
  </div>
  <ul class="plan-list">
    <li>Unlimited E-Certificates</li><li>Unlimited SMS Certificates</li><li>Unlimited Web Banner Certificates</li><li>Unlimited White Label Certiifcate Landing Pages</li><li>Unlimited Website Sticky Bar Certificates</li><li>Unlimited Website Pop Up Certificate</li><li>Unlimited API E-Certificates</li><li>Unlimited Workflow Integration Access</li><li>FREE Warm Lead Letter Templates</li><li>FREE Customer Appreciation Letter Templates</li><li>FREE Professional-Grade Incentive Videos</li><li>FREE Proven Social Media Ad Templates</li><li>FREE High-Converting Banner Ad Templates</li><li>FREE Time-Tested Print Ad Templates</li><li>FREE White Label Redemption Website</li><li>FREE Industry Specific Ad Packs</li><li>FREE Affiliate Program-Earn 50% Commissions</li><li>FREE Eye-Catching Posters, Flyers &amp; Brochures</li><li>Each Certificate</li><li>FREE Step by Step Redemption Guides</li>
  </ul>
  <div class="plan-actions">
    <div class="plan-select"><strong>SELECT</strong><small>Vacation $99</small></div>
    <div class="plan-select"><strong>SELECT</strong><small>Devices $299</small></div>
  </div>
</article>

<article class="plan plan-biannual">
  <div class="plan-body"></div>
  <div class="plan-price">
    <span class="price-label">Vacation &amp; Dining</span><span class="price-value">$490</span>
    <span class="price-split"></span>
    <span class="price-label">Smart Devices</span><span class="price-value">$1,590</span>
  </div>
  <div class="plan-head">
    <p class="plan-kicker">Unlimited Plan</p>
    <h3 class="plan-name">BI ANNUAL</h3>
    <div class="plan-rule"></div>
    <p class="plan-fee">6 Months + $199 One-Time Set-Up Fee</p>
  </div>
  <ul class="plan-list">
    <li>Unlimited E-Certificates</li><li>Unlimited SMS Certificates</li><li>Unlimited Web Banner Certificates</li><li>Unlimited White Label Certiifcate Landing Pages</li><li>Unlimited Website Sticky Bar Certificates</li><li>Unlimited Website Pop Up Certificate</li><li>Unlimited API E-Certificates</li><li>Unlimited Workflow Integration Access</li><li>FREE Warm Lead Letter Templates</li><li>FREE Customer Appreciation Letter Templates</li><li>FREE Professional-Grade Incentive Videos</li><li>FREE Proven Social Media Ad Templates</li><li>FREE High-Converting Banner Ad Templates</li><li>FREE Time-Tested Print Ad Templates</li><li>FREE White Label Redemption Website</li><li>FREE Industry Specific Ad Packs</li><li>FREE Affiliate Program-Earn 50% Commissions</li><li>FREE Eye-Catching Posters, Flyers &amp; Brochures</li><li>Each Certificate</li><li>FREE Step by Step Redemption Guides</li>
  </ul>
  <div class="plan-actions">
    <div class="plan-select"><strong>SELECT</strong><small>Vacation $490</small></div>
    <div class="plan-select"><strong>SELECT</strong><small>Devices $1,590</small></div>
  </div>
</article>

<article class="plan plan-annual">
  <div class="plan-body"></div>
  <div class="plan-price">
    <span class="price-label">Vacation &amp; Dining</span><span class="price-value">$898</span>
    <span class="price-split"></span>
    <span class="price-label">Smart Devices</span><span class="price-value">$2,898</span>
  </div>
  <div class="plan-head">
    <p class="plan-kicker">Unlimited Plan</p>
    <h3 class="plan-name">ANNUAL</h3>
    <div class="plan-rule"></div>
    <p class="plan-fee">12 Months + $199 One-Time Set-Up Fee</p>
  </div>
  <ul class="plan-list">
    <li>Unlimited E-Certificates</li><li>Unlimited SMS Certificates</li><li>Unlimited Web Banner Certificates</li><li>Unlimited White Label Certiifcate Landing Pages</li><li>Unlimited Website Sticky Bar Certificates</li><li>Unlimited Website Pop Up Certificate</li><li>Unlimited API E-Certificates</li><li>Unlimited Workflow Integration Access</li><li>FREE Warm Lead Letter Templates</li><li>FREE Customer Appreciation Letter Templates</li><li>FREE Professional-Grade Incentive Videos</li><li>FREE Proven Social Media Ad Templates</li><li>FREE High-Converting Banner Ad Templates</li><li>FREE Time-Tested Print Ad Templates</li><li>FREE White Label Redemption Website</li><li>FREE Industry Specific Ad Packs</li><li>FREE Affiliate Program-Earn 50% Commissions</li><li>FREE Eye-Catching Posters, Flyers &amp; Brochures</li><li>Each Certificate</li><li>FREE Step by Step Redemption Guides</li>
  </ul>
  <div class="plan-actions">
    <div class="plan-select"><strong>SELECT</strong><small>Vacation $898</small></div>
    <div class="plan-select"><strong>SELECT</strong><small>Devices $2,898</small></div>
  </div>
</article>

<footer class="site-footer">
  <div class="footer-brand"><span class="brand-dot"></span><span class="brand-name">BRIGHT LANE<br>PROMO WORKS</span></div>
  <div class="social"><span></span><span></span><span></span><span></span></div>
  <div class="samples-btn"><strong>GET FREE SAMPLES</strong><em>100% FREE</em></div>

  <div class="footer-col col-contact">
    <h3>CONTACT US</h3>
    <div class="contact-row">
      <svg width="13" height="16" viewBox="0 0 13 16" aria-hidden="true"><path d="M6.5 15s5-5.5 5-9a5 5 0 0 0-10 0c0 3.5 5 9 5 9z" fill="none" stroke="#8893a2" stroke-width="1.2"/><circle cx="6.5" cy="6" r="1.8" fill="none" stroke="#8893a2" stroke-width="1.2"/></svg>
      <b>Bright Lane Promo Group, Inc.</b><br>4410 Harbor View Road Suite 118<br>Seaside, CA 93955
    </div>
    <div class="contact-row">
      <svg width="14" height="14" viewBox="0 0 14 14" aria-hidden="true"><path d="M3 1l2.5 3-1.5 1.5c1 2 2.5 3.5 4.5 4.5L10 8.5l3 2.5-1.5 2C6 13 1 8 1 2.5z" fill="none" stroke="#8893a2" stroke-width="1.2"/></svg>
      USA Office: <b>1-555-014-2286</b><br>International: <b>1-800-555-0147</b><br>Text Us: <b>1-555-014-3390</b>
    </div>
    <div class="contact-row">
      <svg width="14" height="11" viewBox="0 0 14 11" aria-hidden="true"><rect x=".6" y=".6" width="12.8" height="9.8" fill="none" stroke="#8893a2" stroke-width="1.2"/><path d="M.6.6L7 6l6.4-5.4" fill="none" stroke="#8893a2" stroke-width="1.2"/></svg>
      info@brightlanepromoworks.biz
    </div>
    <div class="contact-row">
      <svg width="14" height="14" viewBox="0 0 14 14" aria-hidden="true"><circle cx="7" cy="7" r="6.2" fill="none" stroke="#8893a2" stroke-width="1.2"/><path d="M7 3.5V7l2.5 1.5" fill="none" stroke="#8893a2" stroke-width="1.2"/></svg>
      24/7 Chat Support<br>24/7 Live Answering Service<br>24/7 Email Support<br><span class="hi">Live Phone &amp; SMS Support:</span><br>Monday - Friday 8am - 5pm PST<br><span class="hi">Sat/Sun/Holidays Closed</span>
    </div>
  </div>
  <div class="divider" style="left:678px"></div>

  <div class="footer-col col-quick">
    <h3>QUICK LINKS</h3>
    <ul><li>Home</li><li>The Incentives</li><li>Samples</li><li>Affiliate</li><li>Testimonials</li><li>Faq</li><li>Contact Us</li><li>Redemption Demo Videos</li><li>BLP Distribute Certificate Demo Videos</li></ul>
  </div>
  <div class="divider" style="left:873px"></div>

  <div class="footer-col col-other">
    <h3>OTHER LINKS</h3>
    <ul><li>Hoteliers</li><li>BLP Certificates List</li><li>How To Use BLP Certificates</li><li>Social Incentive Campaign</li><li>Pop Ups &amp; Sticky Bars</li><li>Whitepaper - Increase Sales</li><li>Whitepaper - Improve Sales During Strange Times</li><li>Whitepaper - Boost Website Conversions</li></ul>
  </div>

  <p class="copyright">© 2020 <b>Bright Lane Promo Group, Inc.</b> All Rights Reserved. CST# 4417720 <span class="hi">TCRC#</span> 308811</p>
  <p class="legal">Privacy Policy &nbsp;|&nbsp; Term And Conditions</p>
  <div class="chat">
    <svg width="22" height="20" viewBox="0 0 22 20" aria-hidden="true"><rect x="1" y="1" width="20" height="15" rx="4" fill="#fff"/><path d="M6 7.5c3 3 7 3 10 0" fill="none" stroke="#e5242b" stroke-width="1.6"/></svg>
  </div>
</footer>

</body>
</html>
```